Lumo Habitat Real estate Costa del sol

we need a website for our Company based in Costa del sol, Spain. We sell properties on the spanish coast that is called costa del sol. We are concentrating on exclusive properties and would like the webdesign to show this. In our website we want to have area descriptions of the different areas we sell our Products. We will also implement a searchable database delivered by a third part where all properties for sale in Spain are listed. When looking into the designs we would like our main page to have a overview of the coast where the different areas are shown. Have a look at brightvillarow.com or mykelsa.com to see. The webpage will be presented in 4 languages, English, spanish, Swedish and norwegian, and shall of course also be prepared for social medias. We want an easy Contemporary design but still with an exclusive feeling!
Target Market(s)
Scandinavian and North european Citizens wants to buy a property in Spain
Industry/Entity Type
Real Estate
Number of Pages Required
5+ page
Look and feel

```html
<!DOCTYPE html>
<html lang="en">
<head>
<meta charset="utf-8">
<title>Lumo Habitat – Costa del Sol Real Estate</title>
<link href="https://fonts.googleapis.com/css2?family=Open+Sans:wght@400;600;700&family=Montserrat:wght@600;700&display=swap" rel="stylesheet">
<style>
:root{
  --navy:#1b2778;
  --navy-deep:#141d5e;
  --ink:#333;
  --muted:#666;
  --page:#ececec;
  --panel:#fff;
  --line:#d4d4d4;
  --footer:#2b2b2b;
  --footer-bottom:#1e1e1e;
  --field:#f7f7f7;
}
*{box-sizing:border-box;margin:0;padding:0}
html,body{width:1200px;height:3102px;overflow:hidden}
body{font-family:"Open Sans",Arial,sans-serif;color:var(--ink);background:var(--page);position:relative}
ul{list-style:none}

/* hero */
.hero{position:absolute;left:0;top:0;width:1200px;height:690px;
  background:radial-gradient(ellipse at 55% 55%,#3f8f6c 0%,#2d7b66 18%,#2a6fa6 36%,#1f5aa8 55%,#173f86 80%,#112a5e 100%)}
.brand{position:absolute;left:60px;top:18px;display:flex;align-items:center;gap:12px;
  background:#fff;padding:10px 16px;border-radius:2px}
.brand-mark{width:26px;height:26px;background:var(--navy)}
.brand-name{font-family:"Montserrat",sans-serif;font-weight:700;font-size:22px;color:var(--navy)}
.topline{position:absolute;right:60px;top:24px;display:flex;align-items:center;gap:10px;color:#fff;font-size:15px;font-weight:600}
.social{display:flex;gap:6px}
.social span{width:20px;height:20px;border-radius:50%;background:rgba(255,255,255,.85)}
.nav{position:absolute;right:60px;top:60px;display:flex;gap:4px}
.nav a{display:block;padding:9px 14px;font-size:13px;font-weight:700;color:#fff;text-decoration:none;text-transform:uppercase}
.nav a.active{background:#fff;color:var(--navy)}
.search-tab{position:absolute;left:60px;top:498px;background:var(--navy);color:#fff;font-weight:700;font-size:16px;padding:8px 18px}
.search{position:absolute;left:60px;top:534px;width:1080px;height:118px;background:rgba(230,230,230,.92);
  padding:16px 20px;display:grid;grid-template-columns:repeat(4,1fr);gap:14px 22px}
.select{height:34px;background:var(--field);border:1px solid var(--line);font-size:13px;color:#555;
  display:flex;align-items:center;justify-content:space-between;padding:0 10px}
.select::after{content:"";border:5px solid transparent;border-top-color:#555;margin-top:5px}
.search-btn{height:34px;background:var(--navy);color:#fff;font-weight:700;font-size:13px;display:flex;align-items:center;justify-content:center}

/* welcome */
.welcome{position:absolute;left:0;top:690px;width:1200px;height:690px;background:#fff}
.welcome h1{position:absolute;top:74px;width:100%;text-align:center;font-family:"Montserrat",sans-serif;font-size:40px;font-weight:600;color:#222;letter-spacing:1px}
.welcome .lead{position:absolute;left:220px;top:150px;width:760px;text-align:center;font-size:15px;line-height:1.75;color:var(--muted)}
.cards{position:absolute;left:60px;top:298px;width:1080px;display:flex;gap:48px}
.card{width:328px;height:330px;border:1px solid var(--line);background:#fff;position:relative;overflow:hidden}
.card-photo{height:206px;margin:8px;background:linear-gradient(180deg,#9cc3e6 0%,#c9d9e6 45%,#7f9a6c 80%,#5f7a4e 100%)}
.card h3{font-size:19px;font-weight:700;padding:4px 16px 4px;color:#222}
.card p{font-size:13px;line-height:1.5;color:var(--muted);padding:0 70px 0 16px}
.corner{position:absolute;right:0;bottom:0;width:60px;height:60px}

/* who we are */
.who{position:absolute;left:0;top:1380px;width:1200px;height:520px;background:linear-gradient(90deg,#3b4aa0 0%,var(--navy) 45%,var(--navy-deep) 100%)}
.who-photo{position:absolute;left:0;top:40px;width:560px;height:480px;background:linear-gradient(180deg,#6f7fc4 0%,#56639f 55%,#3d4a7f 100%)}
.who-copy{position:absolute;left:660px;top:80px;width:440px;color:#fff}
.who-copy h2{font-family:"Montserrat",sans-serif;font-size:40px;font-weight:600;letter-spacing:1px;margin-bottom:22px}
.who-copy p{font-size:14px;line-height:1.7;margin-bottom:18px}
.btn-ghost{display:inline-block;background:#9a9a9a;color:#fff;font-weight:700;font-size:14px;padding:10px 22px}

/* listings */
.listings{position:absolute;left:60px;top:2010px;width:750px;height:740px;background:#fff;border:1px solid var(--line)}
.box-head{background:var(--navy);color:#fff;font-weight:700;font-size:16px;padding:10px 18px}
.item{display:flex;gap:20px;padding:17px 18px;border-bottom:1px solid #e3e3e3}
.item:last-child{border-bottom:0}
.thumb{width:130px;height:96px;flex:none;background:linear-gradient(180deg,#a9c7e2 0%,#d4dde4 45%,#7c8f62 100%)}
.item h4{font-size:19px;font-weight:600;color:#222;margin-bottom:4px}
.item p{font-size:12.5px;line-height:1.5;color:var(--muted);width:520px}
.price{font-size:18px;font-weight:700;color:#222;margin-top:6px}

.aside{position:absolute;left:830px;top:2010px;width:310px}
.newsletter{background:#fff;border:1px solid var(--line);height:224px}
.newsletter p{font-size:13px;line-height:1.5;color:var(--muted);padding:14px 16px 10px}
.field{margin:0 16px;height:34px;border:1px solid var(--line);background:var(--field);font-size:13px;color:#999;display:flex;align-items:center;padding:0 10px}
.submit{margin:12px 16px 0 auto;width:90px;height:34px;background:var(--navy-deep);color:#fff;font-weight:700;font-size:13px;display:flex;align-items:center;justify-content:center}
.ad{margin-top:18px;background:#fff;border:1px solid var(--line);height:300px;padding:10px}
.ad-photo{height:150px;background:linear-gradient(180deg,#b9cfe3 0%,#d9cdb5 55%,#6e8a4f 100%)}
.ad h5{font-size:24px;font-weight:700;color:#222;text-align:center;margin-top:10px}
.ad .sub{font-size:12px;letter-spacing:3px;text-align:center;color:#444;margin-top:2px}
.ad .small{font-size:10.5px;line-height:1.4;color:var(--muted);text-align:center;margin-top:8px}
.ad-foot{margin:12px -10px 0;background:#5a9bc4;color:#fff;font-size:10.5px;text-align:center;padding:6px}

/* footer */
.footer{position:absolute;left:0;top:2848px;width:1200px;height:212px;background:var(--footer);color:#cfcfcf}
.footer-cols{display:flex;padding:34px 60px 0;gap:0}
.footer-col{width:216px}
.footer-col h6{font-size:13px;font-weight:700;color:#fff;text-transform:uppercase;margin-bottom:12px}
.footer-col li{font-size:12px;line-height:1.75}
.footer-bottom{position:absolute;left:0;top:3060px;width:1200px;height:42px;background:var(--footer-bottom);color:#aaa;font-size:12px;display:flex;align-items:center;justify-content:center}
</style>
</head>
<body>

<header class="hero" role="img" aria-label="Aerial map view of the Costa del Sol coastline and surrounding sea">
  <div class="brand"><span class="brand-mark"></span><span class="brand-name">Lumo Habitat</span></div>
  <div class="topline">
    <svg width="16" height="16" viewBox="0 0 24 24" fill="#fff"><path d="M6.6 10.8a15.2 15.2 0 0 0 6.6 6.6l2.2-2.2c.3-.3.7-.4 1-.2 1.1.4 2.3.6 3.6.6.6 0 1 .4 1 1V20c0 .6-.4 1-1 1A17 17 0 0 1 3 4c0-.6.4-1 1-1h3.5c.6 0 1 .4 1 1 0 1.3.2 2.5.6 3.6.1.3 0 .7-.2 1z"/></svg>
    <span>+34 900 214 377</span>
    <div class="social"><span></span><span></span><span></span><span></span></div>
  </div>
  <nav class="nav">
    <a class="active" href="#">Home</a><a href="#">Costa</a><a href="#">Services</a><a href="#">About us</a><a href="#">Blog</a><a href="#">Contact us</a>
  </nav>
  <div class="search-tab">Property Search</div>
  <div class="search">
    <div class="select">Select location</div>
    <div class="select">All Types</div>
    <div class="select">Min Price</div>
    <div class="select">Optional Reference</div>
    <div class="select">Min Beds</div>
    <div class="select">Sub-type</div>
    <div class="select">Unlimited</div>
    <div class="search-btn">SEARCH</div>
  </div>
</header>

<section class="welcome">
  <h1>WELCOME TO LUMO HABITAT</h1>
  <p class="lead">This multi-photo template is ideal for homes that show well. Many photos can be featured, allowing you to fully showcase the strengths of your listing. Several pictures in the Contemporary template are definitely worth more than a thousand words. This multi-photo template is ideal for homes that show well. Many photos can be featured, allowing you to fully showcase the strengths of your listing. Several pictures in the Contemporary template are definitely worth more than a thousand words.</p>
  <div class="cards">
    <article class="card">
      <div class="card-photo" role="img" aria-label="Modern villa exterior"></div>
      <h3>View Property Features</h3>
      <p>This multi-photo template is ideal for homes that show well.</p>
      <svg class="corner" viewBox="0 0 60 60"><polygon points="60,0 60,60 0,60" fill="var(--navy)"/><polygon points="44,34 47,42 55,42 49,47 51,55 44,50 37,55 39,47 33,42 41,42" fill="#fff"/></svg>
    </article>
    <article class="card">
      <div class="card-photo" role="img" aria-label="Detached family house with garden"></div>
      <h3>View Photo gallery</h3>
      <p>This multi-photo template is ideal for homes that show well.</p>
      <svg class="corner" viewBox="0 0 60 60"><polygon points="60,0 60,60 0,60" fill="var(--navy)"/><path d="M36 48h16M46 42l6 6-6 6" stroke="#fff" stroke-width="3" fill="none"/></svg>
    </article>
    <article class="card">
      <div class="card-photo" role="img" aria-label="Large stone house with lawn"></div>
      <h3>Request Property Info</h3>
      <p>This multi-photo template is ideal for homes that show well.</p>
      <svg class="corner" viewBox="0 0 60 60"><polygon points="60,0 60,60 0,60" fill="var(--navy)"/><path d="M38 52l4-4 10-10 4 4-10 10-4 4h-4z" fill="#fff"/></svg>
    </article>
  </div>
</section>

<section class="who">
  <div class="who-photo" role="img" aria-label="Two-storey family house with blue tint overlay"></div>
  <div class="who-copy">
    <h2>WHO WE ARE</h2>
    <p>This multi-photo template is ideal for homes that show well. Many photos can be featured, allowing you to fully showcase the strengths of your listing. Several pictures in the Contemporary template are definitely worth more than a thousand words. This multi-photo template is ideal for homes that show well.</p>
    <p>Allowing you to fully showcase the strengths of your listing. Several pictures in the Contemporary template are definitely worth more than a thousand words.</p>
    <span class="btn-ghost">Customer Support</span>
  </div>
</section>

<section class="listings">
  <div class="box-head">Highlighted Properties</div>
  <ul>
    <li class="item"><div class="thumb" role="img" aria-label="Detached villa photo"></div><div><h4>Detached Villa for Sale in Elviria</h4><p>This multi-photo template is ideal for homes that show well. Many photos can be featured, allowing you to fully showcase the strengths of your listing.</p><div class="price">360.000 €</div></div></li>
    <li class="item"><div class="thumb" role="img" aria-label="Detached villa photo"></div><div><h4>Detached Villa for Sale in Elviria</h4><p>This multi-photo template is ideal for homes that show well. Many photos can be featured, allowing you to fully showcase the strengths of your listing.</p><div class="price">360.000 €</div></div></li>
    <li class="item"><div class="thumb" role="img" aria-label="Detached villa photo"></div><div><h4>Detached Villa for Sale in Elviria</h4><p>This multi-photo template is ideal for homes that show well. Many photos can be featured, allowing you to fully showcase the strengths of your listing.</p><div class="price">360.000 €</div></div></li>
    <li class="item"><div class="thumb" role="img" aria-label="Detached villa photo"></div><div><h4>Detached Villa for Sale in Elviria</h4><p>This multi-photo template is ideal for homes that show well. Many photos can be featured, allowing you to fully showcase the strengths of your listing.</p><div class="price">360.000 €</div></div></li>
    <li class="item"><div class="thumb" role="img" aria-label="Detached villa photo"></div><div><h4>Detached Villa for Sale in Elviria</h4><p>This multi-photo template is ideal for homes that show well. Many photos can be featured, allowing you to fully showcase the strengths of your listing.</p><div class="price">360.000 €</div></div></li>
  </ul>
</section>

<aside class="aside">
  <div class="newsletter">
    <div class="box-head">Subscribe Newsletter</div>
    <p>Allowing you to fully showcase the strengths of your listing.</p>
    <div class="field">Your email</div>
    <div class="submit">Submit</div>
  </div>
  <div class="ad">
    <div class="ad-photo" role="img" aria-label="Residence building with gardens"></div>
    <h5>Elmcrest Residence</h5>
    <div class="sub">CARE HOME</div>
    <p class="small">A friendly home offering calm rooms, garden views and caring staff day and night, close to the coast.</p>
    <div class="ad-foot">Call us today for a visit and a warm welcome</div>
  </div>
</aside>

<footer class="footer">
  <div class="footer-cols">
    <div class="footer-col"><h6>Other Countries</h6><ul><li>South Africa</li><li>Belgium</li><li>Ireland</li><li>Greece</li><li>Other</li><li>Sweden</li></ul></div>
    <div class="footer-col"><h6>About Us</h6><ul><li>About Us</li><li>Partnerships</li><li>Brands A-Z</li><li>Affiliate Program</li><li>Press</li><li>Careers</li></ul></div>
    <div class="footer-col"><h6>Customer Services</h6><ul><li>FAQs</li><li>Delivery</li><li>Size Guide</li><li>Payment Methods</li><li>Returns</li><li>Customer Rights</li><li>Legal</li></ul></div>
    <div class="footer-col"><h6>Our Top Categories</h6><ul><li>Coastal Villas</li><li>Town Houses</li><li>Apartments</li><li>Penthouses</li><li>Golf Homes</li><li>New Builds</li><li>Plots</li></ul></div>
    <div class="footer-col"><h6>Our Top Areas</h6><ul><li>Marbella</li><li>Estepona</li><li>Benahavís</li><li>Mijas</li><li>Nerja</li><li>Fuengirola</li></ul></div>
  </div>
</footer>
<div class="footer-bottom">© 2016 Copyright Lumo Habitat. All Rights Reserved.</div>

</body>
</html>
```